Stationery Design Project for import company - Kelvo Trading

We are a import company that sells branded products to large retailers in New Zealand.
We need a simple, professional looking Logo, Business Cards, Email Signature and Letterhead.
Design needs to have some colour in it but nothing too bright or youthful.
The brand is business to business.
The companies name is Kelvo Trading.
I have uploaded some examples of business cards that I like
Also need a powerpoint template
The range of products is diverse so the deign needs to be generic. Please note that the business does not sell to consumers only other businesses
Target Market(s)
Buyers at Retail Companies Head Offices (business to business)
Industry/Entity Type
Business
Look and feel
Each slider illustrates characteristics of the customer's brand and the style your logo design should communicate.

```html
<!DOCTYPE html>
<html lang="en">
<head>
<meta charset="utf-8">
<title>Kelvo Trading — Business Cards</title>
<link rel="stylesheet" href="https://fonts.googleapis.com/css2?family=Cinzel:wght@400&family=Questrial&display=swap">
<style>
  :root {
    --backdrop: #e6e8eb;
    --card-white: #ffffff;
    --card-grey: #eef0f2;
    --brand-blue: #1f9ad6;
    --brand-blue-light: #35b2ea;
    --brand-blue-deep: #0b6ea6;
    --navy: #1c3f73;
    --text-dark: #3a3f45;
    --text-mid: #5f666d;
    --divider: #c9cdd2;
  }
  * { box-sizing: border-box; margin: 0; padding: 0; }
  html, body { width: 1200px; height: 871px; overflow: hidden; }
  body {
    background: var(--backdrop);
    display: flex;
    align-items: center;
    justify-content: center;
    gap: 48px;
  }
  .card {
    position: relative;
    width: 520px;
    height: 300px;
    overflow: hidden;
    box-shadow: 0 6px 18px rgba(0,0,0,0.18);
  }

  /* Contact side */
  .card--contact {
    background: linear-gradient(160deg, var(--card-white) 55%, var(--card-grey) 100%);
  }
  .card--contact .brand {
    position: absolute;
    left: 34px;
    top: 96px;
    display: flex;
    align-items: center;
    gap: 12px;
  }
  .brand-dot {
    width: 30px; height: 30px;
    border-radius: 50%;
    background: var(--brand-blue);
  }
  .brand-rule {
    width: 1px; height: 40px;
    background: var(--divider);
  }
  .brand-name {
    font-family: "Cinzel", serif;
    color: var(--navy);
    font-size: 20px;
    letter-spacing: 1px;
  }
  .person {
    position: absolute;
    right: 40px;
    top: 38px;
    text-align: right;
    font-family: "Questrial", sans-serif;
  }
  .person-name { font-size: 20px; color: var(--navy); }
  .person-role { font-size: 14px; color: var(--text-mid); margin-top: 2px; }
  .contact-list {
    position: absolute;
    left: 36px;
    top: 160px;
    list-style: none;
    font-family: "Questrial", sans-serif;
    font-size: 10.5px;
    line-height: 15px;
    color: var(--text-dark);
  }
  .contact-list .label { color: var(--navy); font-weight: 700; margin-right: 3px; }
  .contact-band { position: absolute; left: 0; bottom: 0; width: 520px; height: 300px; }

  /* Brand side */
  .card--brand {
    background: radial-gradient(ellipse at 30% 20%, var(--brand-blue-light) 0%, var(--brand-blue) 45%, var(--brand-blue-deep) 100%);
  }
  .card--brand .brand {
    position: absolute;
    left: 62px;
    top: 110px;
    display: flex;
    align-items: center;
    gap: 18px;
  }
  .card--brand .brand-dot {
    width: 56px; height: 56px;
    background: var(--card-white);
    opacity: 0.9;
  }
  .card--brand .brand-rule {
    height: 80px;
    background: rgba(255,255,255,0.35);
  }
  .card--brand .brand-name {
    color: var(--card-white);
    font-size: 34px;
    letter-spacing: 1.5px;
  }
</style>
</head>
<body>
  <section class="card card--contact" aria-label="Business card, contact side">
    <svg class="contact-band" viewBox="0 0 520 300" aria-hidden="true">
      <polygon points="0,288 520,262 520,274 0,300" fill="var(--navy)"/>
      <polygon points="0,300 520,274 520,300" fill="var(--brand-blue)"/>
      <polygon points="520,0 520,40 470,0" fill="var(--brand-blue)" opacity="0.85"/>
    </svg>
    <div class="person">
      <p class="person-name">Marcus Halden</p>
      <p class="person-role">President</p>
    </div>
    <div class="brand">
      <span class="brand-dot"></span>
      <span class="brand-rule"></span>
      <span class="brand-name">Kelvo Trading</span>
    </div>
    <ul class="contact-list">
      <li>48 Harbour Lane, Wellington</li>
      <li>6011, New Zealand</li>
      <li><span class="label">P:</span>04 555 0192</li>
      <li><span class="label">C:</span>000 000 0000</li>
      <li><span class="label">F:</span>000 000 0000</li>
      <li><span class="label">E:</span>marcus@kelvotrading.example</li>
      <li>www.kelvotrading.example</li>
    </ul>
  </section>

  <section class="card card--brand" aria-label="Business card, brand side">
    <div class="brand">
      <span class="brand-dot"></span>
      <span class="brand-rule"></span>
      <span class="brand-name">Kelvo Trading</span>
    </div>
  </section>
</body>
</html>
```